VEXMORA, INC. BUSINESS CARD REDESIGN

Attached is an example business card. Name, Title, Address, Contact Information, logo and social media icons are ALL required to be designed into the card. The logo can be modified. An exact replica (or few modifications) of the existing design will be rejected.

Card can either have a blue or white background. Blues and any complimentary color of social media logos that are included on the card.

An example is attached/provided but should not be merely copied or slightly modified.

This should be a new, innovative design relative to the general concept of the existing business card.

Reason: This project has been updated; please utilize the original logo as much as possible. Also because of the high quality of most of the submissions the company requires additional time to reach out with feedback to the top designers for editing and re-submission to determine the finalist. Thank you.

Target Market(s)

B2B (business to business), Television News Stations, Broadcasting, Radio, Magazine and Newspaper Organizations.

Industry/Entity Type

Media

Contact Information for Business Card

Example attached. Company name with exisiting logo (can be altered/edited) in blue (similar to quorble/lintavo blue, but brighter and/or bolder).

Optional two sided card so that just the "VEXMORA" logo is on the front side of the card with contact information on the back side.

Logo Text

VEXMORA

Font styles to use
Sans Serif
Other font styles liked:
• ubuntu, ubuntu bold etc...or similar clean fonts that look great on mobile. Open to use of Google Fonts.

Requirements
Must have
• Must have the following branding integrated into the design (not in any specefic order or verbatim):
• VEXMORA, INC.
• Milo Brandt CEO & Founder
• 83 Wrenfield Brellport, ZK 90217
• mobile: 555.010.0142
• milo@vexmora-mail.test
• https://vexmora-mail.test
• Must also include brand assests (e.g. official logos) of QUORBLE, LINTAVO, MARQEEN, SOLLIVAR, DREVONIX, and KELMITRU
• A clean logo only on the front side is requested (blue or white background). The front side can incorporate the social media icons listed in the brief if designer chooses.
Nice to have
• Card can either have a blue or white background. Blues and any complimentary color of social media logos that are included on the card.
• The card can be double sided so that the logo is on front and contact information is professionally displayed on the back. Not necessarily a requirement but a double-sided design will receive a higher preference.
• An example is attached/provided but should not be merely copied or slightly modified.
• This should be a new, innovative design relative to the general concept of the existing business card.
• Also the brand name with the TM trademark after: for example, Vexmora™
• This (the tm) should be added only after a standalone use of just the word VEXMORA or Vexmora™ AND not Vexmora™, Inc., included in the URL or email address obviously. Thanks :)
Should not have
• Should not have the text spelling of Lintavo, Drevonix, Sollivar, Kelmitru, etc...with the exception of "Marqeen" as it is the approved logo to be integrated.

```html
<!DOCTYPE html>
<html lang="en">
<head>
<meta charset="utf-8">
<title>Vexmora business card</title>
<link rel="stylesheet" href="https://fonts.googleapis.com/css2?family=Ubuntu:wght@400;500;700&display=swap">
<style>
  :root {
    --backdrop: #0d0d0d;
    --brand-blue: #2356a3;
    --accent-cyan: #5cc6ec;
    --card-white: #ffffff;
    --ink-white: #f4f6fb;
  }
  * { box-sizing: border-box; margin: 0; padding: 0; }
  html, body { width: 1200px; height: 1000px; overflow: hidden; }
  body {
    background: var(--backdrop);
    font-family: "Ubuntu", sans-serif;
    position: relative;
  }
  .card {
    position: absolute;
    width: 520px;
    height: 300px;
    overflow: hidden;
  }
  .card--front { left: 50px; top: 330px; background: var(--card-white); }
  .card--back { left: 630px; top: 370px; background: var(--brand-blue); }

  /* front */
  .brand-lockup {
    position: absolute; left: 70px; top: 70px;
    display: flex; flex-direction: column; align-items: center; gap: 10px;
  }
  .brand-square {
    width: 110px; height: 110px; border-radius: 10px;
    background: var(--brand-blue);
  }
  .brand-name {
    font-size: 34px; font-weight: 500; color: var(--brand-blue);
    letter-spacing: 0.5px; line-height: 1;
  }
  .social-cluster {
    position: absolute; left: 310px; top: 108px;
    display: flex; flex-direction: column; align-items: center; gap: 6px;
  }
  .social-row { display: flex; gap: 12px; }
  .social-dot {
    width: 24px; height: 24px; border-radius: 50%;
    background: var(--brand-blue);
  }
  .social-handle {
    font-size: 14px; font-weight: 500; color: var(--brand-blue);
  }

  /* back */
  .back-decoration {
    position: absolute; left: -70px; top: 70px;
    width: 230px; height: 230px; border-radius: 16px;
    background: var(--card-white);
    transform: rotate(-12deg);
  }
  .contact-block {
    position: absolute; left: 250px; top: 48px;
    color: var(--ink-white);
  }
  .person-name { font-size: 22px; font-weight: 700; color: var(--accent-cyan); }
  .person-title { font-size: 14px; margin-top: 2px; }
  .company-name {
    font-size: 19px; font-weight: 500; color: var(--accent-cyan);
    margin-top: 14px;
  }
  .contact-list { list-style: none; margin-top: 12px; font-size: 15px; }
  .contact-list li {
    display: flex; align-items: center; gap: 8px; margin-bottom: 5px;
  }
  .contact-icon { width: 14px; height: 14px; flex: none; }
  .address { font-size: 15px; line-height: 1.25; margin-top: 6px; }
</style>
</head>
<body>
  <section class="card card--front" aria-label="Card front">
    <div class="brand-lockup">
      <div class="brand-square" aria-hidden="true"></div>
      <span class="brand-name">vexmora</span>
    </div>
    <div class="social-cluster">
      <div class="social-row">
        <span class="social-dot" role="img" aria-label="Quorble badge"></span>
        <span class="social-dot" role="img" aria-label="Lintavo badge"></span>
        <span class="social-dot" role="img" aria-label="Drevonix badge"></span>
      </div>
      <span class="social-handle">@vexmora</span>
      <div class="social-row">
        <span class="social-dot" role="img" aria-label="Sollivar badge"></span>
        <span class="social-dot" role="img" aria-label="Kelmitru badge"></span>
        <span class="social-dot" role="img" aria-label="Marqeen badge"></span>
      </div>
    </div>
  </section>

  <section class="card card--back" aria-label="Card back">
    <div class="back-decoration" aria-hidden="true"></div>
    <div class="contact-block">
      <p class="person-name">Milo Brandt</p>
      <p class="person-title">CEO &amp; Founder</p>
      <p class="company-name">Vexmora, Inc</p>
      <ul class="contact-list">
        <li>
          <svg class="contact-icon" viewBox="0 0 14 14" aria-hidden="true"><rect x="3.5" y="1" width="7" height="12" rx="1.5" fill="none" stroke="#5cc6ec" stroke-width="1.4"/><circle cx="7" cy="11" r="0.8" fill="#5cc6ec"/></svg>
          555.010.0142
        </li>
        <li>
          <svg class="contact-icon" viewBox="0 0 14 14" aria-hidden="true"><rect x="1" y="3" width="12" height="8" fill="#5cc6ec"/><path d="M1 3 L7 8 L13 3" fill="none" stroke="#2356a3" stroke-width="1.2"/></svg>
          milo@vexmora-mail.test
        </li>
        <li>
          <svg class="contact-icon" viewBox="0 0 14 14" aria-hidden="true"><g fill="none" stroke="#5cc6ec" stroke-width="1.2"><circle cx="7" cy="7" r="5.8"/><ellipse cx="7" cy="7" rx="2.6" ry="5.8"/><path d="M1.2 7 H12.8"/></g></svg>
          www.vexmora-mail.test
        </li>
      </ul>
      <p class="address">83 Wrenfield Brellport<br>ZK 90217</p>
    </div>
  </section>
</body>
</html>
```